Silver Kettle Studio Marketing Postcard

I need a 2 sided A6 postcard to distribute to potential clients. The postcard will include the business logo and information about the service we provide and contact information. I want it to be stylish and to compliment the business card. I've attached the business card and logo files as well as some text to use. I have other source files (.eps and.ai) if required please message me. I don't need the postal address or my position included on the postcard.
I am open to portrait or landscape designs, whatever you think is most stylish and eye catching.

```html
<!DOCTYPE html>
<html lang="en">
<head>
<meta charset="utf-8">
<title>Silver Kettle Studio – Postcard</title>
<link rel="stylesheet" href="https://fonts.googleapis.com/css2?family=Didact+Gothic&family=Montserrat:wght@300;600;700&family=Questrial&display=swap">
<style>
  :root {
    --page-bg: #e9e7e4;
    --navy: #0f3050;
    --blue-light: #1f4d74;
    --blue-dark: #0d2c47;
    --green: #8cc63f;
    --green-light: #a3d154;
    --green-deep: #74ad34;
    --ink-dark: #0f2a3f;
    --white: #ffffff;
    --photo-light: #d9d6d3;
    --photo-mid: #8e8985;
    --photo-dark: #3a3634;
    --rule: #1a1a1a;
  }
  * { margin: 0; padding: 0; box-sizing: border-box; }
  html, body {
    width: 806px; height: 1200px; overflow: hidden;
    background: var(--page-bg);
  }
  .postcard {
    position: absolute;
    overflow: hidden;
    box-shadow: 0 3px 10px rgba(0,0,0,0.25);
  }

  /* ---------- Front ---------- */
  .postcard--front {
    left: 57px; top: 72px; width: 706px; height: 500px;
    background: linear-gradient(180deg, var(--blue-light), var(--blue-dark));
  }
  .front__photo {
    position: absolute; left: 0; top: 0; width: 470px; height: 100%;
    background:
      radial-gradient(ellipse 180px 90px at 250px 300px, var(--photo-dark), transparent 70%),
      radial-gradient(ellipse 150px 70px at 180px 290px, var(--photo-mid), transparent 75%),
      linear-gradient(160deg, var(--photo-light) 0%, var(--photo-mid) 60%, var(--photo-dark) 100%);
    -webkit-mask-image: linear-gradient(90deg, #000 80%, transparent 100%);
            mask-image: linear-gradient(90deg, #000 80%, transparent 100%);
  }
  .front__title {
    position: absolute; left: 18px; top: 28px;
    font-family: "Montserrat", sans-serif;
    color: var(--white);
    text-shadow: 0 1px 3px rgba(0,0,0,0.45);
    line-height: 1;
  }
  .front__title-light { display: block; font-weight: 300; font-size: 44px; letter-spacing: 0.5px; }
  .front__title-bold { display: block; font-weight: 600; font-size: 52px; margin-top: 6px; }
  .front__brand {
    position: absolute; left: 468px; top: 210px; width: 230px;
    font-family: "Questrial", sans-serif;
    color: var(--green);
    font-size: 40px; line-height: 1.1;
  }

  /* ---------- Back ---------- */
  .postcard--back {
    left: 57px; top: 628px; width: 700px; height: 497px;
    background: var(--white);
  }
  .back__panel { position: absolute; inset: 0; }
  .back__content {
    position: absolute; left: 20px; top: 36px; width: 330px;
    font-family: "Didact Gothic", sans-serif;
  }
  .back__headline {
    font-family: "Montserrat", sans-serif;
    font-weight: 700; font-size: 15.5px; line-height: 22px;
    color: var(--ink-dark); text-transform: uppercase;
  }
  .back__intro {
    margin-top: 17px; color: var(--white);
    font-size: 14.2px; line-height: 21.5px;
  }
  .back__services {
    list-style: none; margin-top: 13px;
    display: grid; grid-template-columns: 192px 1fr; row-gap: 2px;
    color: var(--white); font-size: 15px;
  }
  .back__services li { display: flex; align-items: center; gap: 6px; }
  .back__services li::before {
    content: ""; width: 8px; height: 8px; border-radius: 50%;
    background: var(--ink-dark);
  }
  .back__tagline {
    margin-top: 14px; color: var(--white);
    font-family: "Montserrat", sans-serif; font-weight: 600; font-size: 13px;
  }
  .back__contact { margin-top: 10px; padding-left: 4px; color: var(--ink-dark); }
  .back__contact-lead { font-size: 14px; }
  .back__contact-call { font-size: 15px; padding-left: 10px; margin-top: 2px; }
  .back__contact-list { list-style: none; margin-top: 2px; font-size: 11px; line-height: 17px; }
  .back__contact-list li { display: flex; align-items: center; gap: 6px; }
  .back__contact-list svg { width: 8px; height: 8px; fill: var(--ink-dark); }
  .back__signoff {
    position: absolute; left: 20px; top: 450px;
    font-family: "Questrial", sans-serif;
    font-size: 29px; color: var(--white); letter-spacing: 0.3px;
  }
  .back__stamp {
    position: absolute; left: 595px; top: 96px; width: 68px; height: 68px;
    border: 1.5px solid var(--rule);
  }
  .back__address-line {
    position: absolute; left: 451px; width: 235px; height: 0;
    border-top: 1.5px solid var(--rule);
  }
</style>
</head>
<body>

<section class="postcard postcard--front">
  <div class="front__photo" role="img" aria-label="Black and white close-up photograph of computer mice on a desk"></div>
  <h1 class="front__title">
    <span class="front__title-light">TECHNOLOGY</span>
    <span class="front__title-bold">EXPLAINED</span>
  </h1>
  <p class="front__brand">Silver Kettle Studio</p>
</section>

<section class="postcard postcard--back">
  <svg class="back__panel" width="700" height="497" viewBox="0 0 700 497" aria-hidden="true">
    <defs>
      <linearGradient id="panelGreen" x1="0" y1="0" x2="0" y2="1">
        <stop offset="0" stop-color="#a3d154"/>
        <stop offset="1" stop-color="#74ad34"/>
      </linearGradient>
    </defs>
    <path d="M0 0 H255 C330 30 370 110 365 200 C360 290 320 380 360 497 H0 Z" fill="url(#panelGreen)"/>
  </svg>

  <div class="back__content">
    <h2 class="back__headline">Do you feel frustrated<br>by computers, TVs, phones,<br>tablets and countless other<br>digital devices?</h2>
    <p class="back__intro">Silver Kettle Studio is here to help. From a simple computer health check to the purchase and installation of home networks and digital services. We also give useful product advice and maintenance tips.</p>
    <ul class="back__services">
      <li>On site support</li>
      <li>Advice</li>
      <li>Installation</li>
      <li>Education</li>
    </ul>
    <p class="back__tagline">Let us help you tame your digital world</p>
    <div class="back__contact">
      <p class="back__contact-lead">Phone conversations are free</p>
      <p class="back__contact-call">SO CALL Milo</p>
      <ul class="back__contact-list">
        <li><svg viewBox="0 0 10 10"><path d="M2 0 L4 2.5 L3 3.7 Q4.5 6 6.3 7 L7.5 6 L10 8 L8.5 10 Q2 9 0 1.5 Z"/></svg>0400 555 019</li>
        <li><svg viewBox="0 0 10 10"><path d="M0 2 H10 V8 H0 Z M0 2 L5 5.5 L10 2" stroke="#fff" stroke-width="0.8"/></svg>milo@silverkettlestudio.com.au</li>
        <li><svg viewBox="0 0 10 10"><circle cx="5" cy="5" r="5"/></svg>www.silverkettlestudio.com.au</li>
      </ul>
    </div>
  </div>

  <p class="back__signoff">PROBLEMS SOLVED!</p>

  <div class="back__stamp"></div>
  <div class="back__address-line" style="top:247px"></div>
  <div class="back__address-line" style="top:282px"></div>
  <div class="back__address-line" style="top:317px"></div>
</section>

</body>
</html>
```